Artist business cards needed, happy acrylic painter

I'd like a business card I can hand out to people interested in my paintings. I'd like a logo that includes elements of my painting. I have shared a collection that may be used at https://snaplink.example/photos/7xQpLmR3Tz8vBn2K
I get my vibe and the type of art I create, you can also see my active Circle Net account: https://circlesnet.example/+MarlaVintner

Target Market(s)

people interested in art

Industry/Entity Type

Artists

Contact Information for Business Card

Marla Vintner
425-736-1048
marlavintner@quillpost.com
marlavintner@quillpost.com
www.marlavintner-studio.com

Font styles to use
Sans Serif
Decorative
Script

Requirements
Must have
• 1. Colors that are represented in my paintings
• 2. Elements from my paintings: Link to the cloud locker with my art: https://snaplink.example/photos/7xQpLmR3Tz8vBn2K
• 3. Flower(s)
• 4. A box on the back that's outlined so a note could be added. I've attached a photo of a business card my friend uses for her floral design company as an example of the back of the card with the quote and a box and business name (Marla Vintner).
• 4. I'd like to have this quote on the back of the card too.
• "I must have flowers, always and always."
• ~Anton Brisle
Nice to have
• In smaller font
• If it fits, links to my other social media:
• https://circlesnet.example/+MarlaVintner
• https://www.friendwall.example/marlavintnerartist/
Should not have
• A dark background

```html
<!DOCTYPE html>
<html lang="en">
<head>
<meta charset="utf-8">
<title>Marla Vintner – Business Card</title>
<link rel="stylesheet" href="https://fonts.googleapis.com/css2?family=Alegreya+Sans:ital,wght@1,400;1,700&family=Kaushan+Script&family=Quicksand:wght@400;500&display=swap">
<style>
  :root {
    --page: #ece8e1;
    --paper: #ffffff;
    --plum: #8a3d9c;
    --plum-soft: #a467b3;
    --teal: #2fa38a;
    --band: rgba(150, 205, 170, 0.72);
    --ink-light: #ffffff;
    --paint-lilac: #d9c8e4;
    --paint-mint: #bfe3c4;
    --paint-green: #7cc46f;
    --paint-pink: #e8b9d3;
    --paint-blue: #9fb3d8;
  }
  * { box-sizing: border-box; margin: 0; padding: 0; }
  html, body { width: 1200px; height: 950px; overflow: hidden; }
  body {
    background: var(--page);
    display: flex;
    align-items: center;
    justify-content: center;
    gap: 50px;
    font-family: "Quicksand", sans-serif;
  }
  .card {
    border-radius: 22px;
    position: relative;
    overflow: hidden;
    box-shadow: 0 6px 18px rgba(0,0,0,0.18);
    flex: none;
  }

  /* ---------- back (portrait) ---------- */
  .card-back {
    width: 380px;
    height: 640px;
    background: var(--paper);
  }
  .quote {
    position: absolute;
    top: 26px;
    left: 30px;
    right: 30px;
    text-align: right;
    font-family: "Alegreya Sans", sans-serif;
    font-style: italic;
    font-size: 28px;
    line-height: 1.05;
    color: var(--plum);
  }
  .notes-box {
    position: absolute;
    left: 30px;
    top: 112px;
    width: 270px;
    height: 300px;
    border: 3px solid var(--teal);
    border-radius: 30px;
  }
  .notes-label {
    position: absolute;
    top: 12px;
    left: 22px;
    font-size: 13px;
    color: var(--plum-soft);
  }
  .bouquet {
    position: absolute;
    top: 100px;
    right: 22px;
    width: 86px;
    height: 86px;
    border-radius: 40% 40% 30% 30%;
    background: radial-gradient(circle at 50% 40%, var(--paint-pink), var(--paint-lilac) 45%, var(--paint-blue) 70%, rgba(255,255,255,0) 72%);
  }
  .attribution {
    position: absolute;
    right: 40px;
    top: 452px;
    font-family: "Alegreya Sans", sans-serif;
    font-style: italic;
    font-weight: 700;
    font-size: 30px;
    color: var(--plum);
  }
  .social-links {
    position: absolute;
    left: 30px;
    right: 20px;
    bottom: 34px;
    font-size: 13px;
    line-height: 1.5;
    color: var(--plum-soft);
    white-space: nowrap;
  }

  /* ---------- front ---------- */
  .card-front {
    width: 700px;
    height: 400px;
    background: var(--paper);
  }
  .painting {
    position: absolute;
    inset: 0;
    background:
      radial-gradient(ellipse at 20% 25%, var(--paint-pink) 0, rgba(232,185,211,0) 30%),
      radial-gradient(ellipse at 75% 20%, var(--paint-lilac) 0, rgba(217,200,228,0) 35%),
      radial-gradient(ellipse at 80% 85%, var(--paint-green) 0, rgba(124,196,111,0) 40%),
      radial-gradient(ellipse at 25% 85%, var(--paint-blue) 0, rgba(159,179,216,0) 35%),
      linear-gradient(180deg, #f3eef5 0%, var(--paint-mint) 60%, #a9d898 100%);
  }
  .contact-band {
    position: absolute;
    left: 0;
    right: 0;
    top: 110px;
    height: 190px;
    background: var(--band);
    display: flex;
    flex-direction: column;
    justify-content: center;
    padding-left: 250px;
    color: var(--ink-light);
  }
  .name {
    font-family: "Kaushan Script", cursive;
    font-weight: 400;
    font-size: 38px;
    letter-spacing: 1px;
    margin-bottom: 6px;
  }
  .contact-line {
    font-size: 21px;
    line-height: 1.3;
    font-weight: 500;
  }
</style>
</head>
<body>

  <section class="card card-back" aria-label="Card back">
    <p class="quote">I must have flowers,<br>always and always.</p>
    <div class="notes-box">
      <span class="notes-label">Notes :</span>
    </div>
    <div class="bouquet" role="img" aria-label="Painted bouquet of purple and blue flowers"></div>
    <p class="attribution">~Anton Brisle</p>
    <div class="social-links">
      <p>circlesnet.example/+MarlaVintner</p>
      <p>www.friendwall.example/marlavintnerartist/</p>
    </div>
  </section>

  <section class="card card-front" aria-label="Card front">
    <div class="painting" role="img" aria-label="Acrylic painting of pastel pink, lilac and blue flowers on green stems"></div>
    <div class="contact-band">
      <h1 class="name">Marla Vintner</h1>
      <p class="contact-line">425-736-1048</p>
      <p class="contact-line">marlavintner@quillpost.com</p>
      <p class="contact-line">www.marlavintner-studio.com</p>
    </div>
  </section>

</body>
</html>
```